Design logo, business cards, and web page for new web and bi development consulting company

I've started a Web and Business Intelligence development consulting company. We develop on Quorvantel's stack, Vantor Sudio and Qendra Server. We develop responsive web sites and business intelligence platforms. I plan on focusing on small to medium sized business as my client base. I need a logo, business cards, and a one page web site. We will do more with the web site with you in the next six months if the business survives. The name of the company is Belvorq Linkage Solutions, Belvorq for short.

Target Market(s)

small to medium sized businesses

Industry/Entity Type

Business

Contact Information for Business Card

logo
name
title
email
phone

Logo Text

Belvorq Linkage Solutions - web and data solutions

Coding

Coded - Design and coding required

Number of Pages Required

1 page

Font styles to use
Sans Serif

Colors
0355a3
0092cd
00a88f
6b449b

Requirements
Nice to have
• web and data solutions

```html
<!DOCTYPE html>
<html lang="en">
<head>
<meta charset="utf-8">
<title>Belvorq Linkage Solutions</title>
<link rel="stylesheet" href="https://fonts.googleapis.com/css2?family=Roboto+Slab:wght@300;400;700&family=Arimo:wght@400;700&display=swap">
<style>
  :root {
    --brand-blue: #0a7cc4;
    --card-blue: #0079c1;
    --text-blue: #1a7fc0;
    --nav-green: #6fc09a;
    --footer-green: #8fcdb0;
    --slogan-green: #3fae7c;
    --body-grey: #444444;
    --panel-white: #ffffff;
    --card-border: #cfcfcf;
    --wash-white: #ffffff;
    --wash-green: #dcf0e5;
    --wash-green-deep: #c9e8d7;
    --leaf-blue-light: rgba(200, 232, 248, .75);
    --leaf-blue: rgba(168, 216, 240, .75);
    --slab: "Roboto Slab", serif;
    --sans: "Arimo", sans-serif;
  }
  * { box-sizing: border-box; margin: 0; padding: 0; }
  html, body { width: 1200px; height: 1002px; overflow: hidden; background: #ffffff; }
  .page { position: relative; width: 1200px; height: 1002px; overflow: hidden; font-family: var(--slab); }
  .abs { position: absolute; }

  .backdrop {
    left: 0; top: 0; width: 1200px; height: 840px;
    background:
      radial-gradient(ellipse 420px 520px at 1200px 560px, var(--wash-green-deep), rgba(220,240,229,0) 100%),
      radial-gradient(ellipse 700px 340px at 700px 0px, var(--wash-green), rgba(220,240,229,0) 100%),
      linear-gradient(120deg, var(--wash-white) 0%, #eaf6ef 35%, #f7fbf9 60%, #eef8f2 100%);
  }
  .leaf-wash {
    left: 112px; width: 393px; border-radius: 40px 4px 60px 4px;
    background: linear-gradient(135deg, var(--leaf-blue-light), var(--leaf-blue));
  }
  .leaf-top { top: 284px; height: 262px; }
  .leaf-bottom { top: 562px; height: 258px; }

  .brand { left: 137px; top: 112px; }
  .brand-row { display: flex; align-items: center; gap: 8px; }
  .brand-dot { width: 40px; height: 40px; border-radius: 50%; background: var(--brand-blue); }
  .brand-name { font-family: var(--slab); font-weight: 700; font-size: 46px; color: var(--brand-blue); line-height: 1; letter-spacing: 1px; }
  .brand-tagline { font-family: var(--slab); font-weight: 300; font-size: 27px; color: var(--slogan-green); margin-top: 4px; line-height: 1.1; white-space: nowrap; }

  .main-nav { left: 676px; top: 116px; display: flex; gap: 40px; font-family: var(--sans); font-size: 22px; color: var(--nav-green); }

  .section-title { font-family: var(--slab); font-weight: 400; font-size: 22px; color: var(--text-blue); letter-spacing: .3px; white-space: nowrap; }
  .section-copy { font-family: var(--slab); font-weight: 300; font-size: 15px; line-height: 19.4px; color: var(--text-blue); white-space: nowrap; }
  .about { left: 158px; top: 320px; }
  .about .section-copy { margin-top: 26px; }
  .contact-us { left: 158px; top: 617px; }
  .contact-us .section-copy { margin-top: 16px; }

  .solutions-panel { left: 605px; top: 281px; width: 406px; height: 512px; background: var(--panel-white); }
  .solutions-title { left: 629px; top: 320px; }
  .solutions-copy { color: var(--body-grey); }
  .sol-a { left: 629px; top: 374px; }
  .sol-b { left: 629px; top: 509px; }
  .sol-c { left: 629px; top: 606px; }

  .mini-blue { left: 788px; top: 337px; width: 203px; height: 113px; background: var(--card-blue); display: flex; flex-direction: column; align-items: center; justify-content: center; gap: 6px; }
  .mini-blue .dot { width: 26px; height: 26px; border-radius: 50%; background: #ffffff; }
  .mini-blue .word { font-family: var(--slab); font-size: 12px; color: #cfe6f5; letter-spacing: 1px; }

  .mini-card { left: 793px; top: 592px; width: 198px; height: 110px; background: #fff; border: 1px solid var(--card-border); padding: 9px 0 0 20px; color: var(--text-blue); white-space: nowrap; }
  .mini-card .co { font-size: 9.5px; }
  .mini-card .sub { font-family: var(--sans); font-size: 6.5px; }
  .mini-card .nm { font-size: 14px; font-weight: 700; color: var(--brand-blue); margin: 8px 0 0 34px; }
  .mini-card .ho { font-family: var(--sans); font-size: 6px; margin-top: 16px; }

  .card-front { left: 860px; top: 638px; width: 340px; height: 188px; background: var(--card-blue); display: flex; flex-direction: column; align-items: center; padding-top: 24px; }
  .card-front .dot { width: 84px; height: 84px; border-radius: 50%; background: #ffffff; }
  .card-front .word { font-family: var(--slab); font-weight: 300; font-size: 34px; color: #e6f2fa; letter-spacing: 3px; margin-top: 12px; }

  .card-back { left: 768px; top: 797px; width: 332px; height: 184px; background: #fff; border: 1px solid var(--card-border); color: var(--text-blue); white-space: nowrap; }
  .card-back .faint { position: absolute; right: 18px; top: 14px; width: 112px; height: 112px; border-radius: 50%; background: #dcebf7; opacity: .7; }
  .card-back .co { position: absolute; left: 35px; top: 15px; font-size: 14.5px; }
  .card-back .sub { position: absolute; left: 36px; top: 32px; font-family: var(--sans); font-size: 11px; }
  .card-back .person { position: absolute; left: 0; right: 0; top: 60px; text-align: center; padding-left: 30px; }
  .card-back .person-name { font-family: var(--sans); font-weight: 700; font-size: 24px; color: var(--brand-blue); line-height: 1; }
  .card-back .person-role { font-family: var(--sans); font-size: 14px; margin-top: 2px; }
  .card-back .office { position: absolute; left: 42px; top: 129px; font-family: var(--sans); font-size: 9px; }
  .card-back .office i { display: block; width: 68px; border-bottom: 1px dotted var(--text-blue); height: 11px; }
  .card-back .reach { position: absolute; right: 24px; top: 138px; text-align: right; font-family: var(--sans); font-size: 9.5px; line-height: 12px; }

  .footer-links { font-family: var(--sans); font-size: 18px; color: var(--footer-green); line-height: 36px; }
  .footer-col-a { left: 464px; top: 851px; }
  .footer-col-b { left: 643px; top: 851px; }
</style>
</head>
<body>
<div class="page">
  <div class="abs backdrop" role="img" aria-label="Soft green flowing background wash"></div>
  <div class="abs leaf-wash leaf-top" role="img" aria-label="Translucent blue leaf shape behind the about section"></div>
  <div class="abs leaf-wash leaf-bottom" role="img" aria-label="Translucent blue leaf shape behind the contact section"></div>

  <header class="abs brand">
    <div class="brand-row"><span class="brand-dot"></span><span class="brand-name">BELVORQ</span></div>
    <div class="brand-tagline">Linkage Solutions</div>
  </header>

  <nav class="abs main-nav"><span>HOME</span><span>ABOUT</span><span>CONTACT</span></nav>

  <section class="abs about">
    <h2 class="section-title">ABOUT US</h2>
    <p class="section-copy">&nbsp;Web and Business Intelligence<br>development consulting company<br>Web and Business Intelligence<br>development consulting company<br>Web and Business Intelligence<br>development consulting company</p>
  </section>

  <section class="abs contact-us">
    <h2 class="section-title">CONTACT US</h2>
    <p class="section-copy">&nbsp;We develop on Quorvantel's stack,<br>Vantor Sudio and Qendra Server.<br>We develop responsive web sites<br>and business intelligence platforms</p>
  </section>

  <div class="abs solutions-panel"></div>
  <h2 class="abs section-title solutions-title">SOLUTIONS</h2>
  <p class="abs section-copy solutions-copy sol-a">&nbsp;We develop on<br>Quorvantel's stack,<br>Vantor Sudio and<br>Qendra Server.<br>We develop responsive<br>web sites and business intelligence platforms</p>
  <p class="abs section-copy solutions-copy sol-b">&nbsp;We develop on Quorvantel's stack,<br>Vantor Sudio and Qendra Server.<br>We develop responsive web sitesand business<br>intelligence platforms.</p>
  <p class="abs section-copy solutions-copy sol-c">We develop<br>on Quorvantel's<br>stack,<br>Vantor Sudio and<br>Qendra Server.<br>We develop responsive web sites<br>and business intelligence platforms.</p>

  <div class="abs mini-blue"><span class="dot"></span><span class="word">BELVORQ</span></div>
  <div class="abs mini-card">
    <div class="co">Belvorq Linkage Solutions</div>
    <div class="sub">Web and data solutions</div>
    <div class="nm">Dorian Vale</div>
    <div class="ho">Head office</div>
  </div>

  <div class="abs card-front"><span class="dot"></span><span class="word">BELVORQ</span></div>

  <div class="abs card-back">
    <span class="faint"></span>
    <div class="co">Belvorq Linkage Solutions</div>
    <div class="sub">Web and data solutions</div>
    <div class="person">
      <div class="person-name">Dorian Vale</div>
      <div class="person-role">General Manager</div>
    </div>
    <div class="office">Head office<i></i><i></i></div>
    <div class="reach">005550148822<br>dorian.vale@belvorq.com</div>
  </div>

  <nav class="abs footer-links footer-col-a"><div>FAQ</div><div>SITE MAP</div><div>HELP</div></nav>
  <nav class="abs footer-links footer-col-b"><div>CONTACT</div><div>PARTNERSHIP</div><div>LINKS</div></nav>
</div>
</body>
</html>
```